Simple one page Wordpress website

We need a quick turnaround single page wordpress website.
The design needs to be very simple and clean.
We already have some design assets (logos and colours etc) and some draft copy for the page.

We need all the files for us to be able to create a wordpress site. We can do this ourselves and we will host it.

```html
<!DOCTYPE html>
<html lang="en">
<head>
<meta charset="utf-8">
<title>Pawlytix</title>
<link rel="stylesheet" href="https://fonts.googleapis.com/css2?family=Fira+Sans:wght@400;500;600;700&family=Fira+Sans+Condensed:wght@500;600&display=swap">
<style>
:root{
  --navy:#1d3a5c;
  --green:#7c9a1c;
  --green-dark:#5f7a12;
  --blue:#3d6ca3;
  --blue-deep:#2c5488;
  --footer:#26362e;
  --text:#4a4f55;
  --light:#f3f4f2;
  --white:#ffffff;
}
*{margin:0;padding:0;box-sizing:border-box}
html,body{width:1200px;height:4484px;overflow:hidden}
body{position:relative;font-family:"Fira Sans",sans-serif;color:var(--text);background:var(--white)}
.abs{position:absolute}
/* header */
.site-header{left:0;top:0;width:1200px;height:120px;background:var(--white);border-top:6px solid var(--blue)}
.brand{left:110px;top:26px;font-family:"Fira Sans",sans-serif;font-weight:600;font-size:52px;letter-spacing:2px;color:var(--blue-deep);line-height:1}
.main-nav{right:106px;top:52px;display:flex;gap:26px;font-family:"Fira Sans Condensed",sans-serif;font-weight:500;font-size:15px;color:var(--navy);text-transform:uppercase}
.main-nav .active{color:var(--green);border-bottom:2px solid var(--green);padding-bottom:4px}
/* hero */
.hero-photo{left:0;top:120px;width:1200px;height:740px;background:linear-gradient(100deg,#f2f1ee 0%,#e6e2da 35%,#b89a72 55%,#d8d4cc 75%,#9fb6c7 100%)}
.hero-title{left:110px;top:350px;font-family:"Fira Sans Condensed",sans-serif;font-weight:600;font-size:64px;color:var(--navy);line-height:1}
.hero-sub{left:112px;top:435px;width:330px;font-size:15px;line-height:1.5;color:#2f3338}
.btn{display:inline-flex;align-items:center;justify-content:center;border-radius:30px;font-weight:600;text-transform:uppercase}
.hero-btn{left:112px;top:510px;width:170px;height:52px;background:var(--green);color:var(--white);font-size:15px}
.hero-dots{left:570px;top:824px;display:flex;gap:10px}
.hero-dots span{width:12px;height:12px;border-radius:50%;background:rgba(255,255,255,.6)}
.hero-dots span.on{background:var(--white)}
/* shared */
.section-title{font-family:"Fira Sans Condensed",sans-serif;font-weight:600;color:var(--navy);line-height:1;text-transform:uppercase}
.divider{display:block;margin-top:12px}
.rounded-photo{border-radius:60px 0 60px 0;box-shadow:0 18px 40px rgba(0,0,0,.18)}
/* mission */
.mission-photo{left:152px;top:940px;width:448px;height:580px;background:linear-gradient(160deg,#c9c2b6,#8e8579 50%,#e8e4dc)}
.mission-title{left:676px;top:1010px;font-size:50px}
.mission-copy{left:676px;top:1110px;width:380px;font-size:20px;line-height:1.55;color:#6b6f73}
.mission-copy .g{color:var(--green);font-weight:600;font-size:23px}
.mission-copy .b{color:var(--blue-deep);font-weight:600;font-size:26px}
.mission-copy .n{color:var(--navy);font-weight:600;font-size:25px}
/* capabilities */
.capabilities{left:0;top:1540px;width:1200px;height:820px;background:var(--light)}
.cap-title{left:110px;top:1655px;font-size:48px}
.cap-body{left:112px;top:1745px;width:480px;font-size:14.5px;line-height:1.55;color:#555a5f}
.cap-body p{margin-bottom:14px}
.cap-body .lead{color:var(--green);font-weight:600;font-size:16px;margin-bottom:6px}
.cap-list{list-style:none;margin:6px 0 20px}
.cap-list li{display:flex;align-items:center;gap:12px;margin-bottom:9px}
.cap-list svg{flex:none}
.cap-mail{color:var(--green);font-weight:600;font-size:22px;text-decoration:underline}
.cap-photo{left:628px;top:1700px;width:444px;height:580px;background:linear-gradient(150deg,#6f6d66,#3f4a46 45%,#7b8f5e 75%,#a8a59c)}
/* joint venture */
.jv{left:0;top:2360px;width:1200px;height:600px;background:var(--blue)}
.jv-photo{left:0;top:2360px;width:520px;height:600px;background:linear-gradient(90deg,rgba(200,205,210,.55),rgba(61,108,163,.0)),linear-gradient(180deg,#6f8fb6,#4b76a8)}
.jv-title{left:600px;top:2420px;font-size:42px;color:var(--white)}
.jv-copy{left:600px;top:2510px;width:500px;font-size:14.5px;line-height:1.6;color:#e8eef6}
.jv-copy p{margin-bottom:20px}
/* team */
.team-title{left:0;top:3010px;width:1200px;text-align:center;font-size:44px}
.team-title .divider{margin:12px auto 0}
.team-card{top:3110px;width:232px;height:450px;background:var(--white);box-shadow:0 6px 22px rgba(0,0,0,.12);text-align:center}
.team-photo{height:290px;background:linear-gradient(170deg,#c9a587,#8b6a52 60%,#5a4c44)}
.team-name{margin-top:16px;font-family:"Fira Sans Condensed",sans-serif;font-weight:600;font-size:17px;color:#333}
.team-bio{margin:8px auto 0;width:170px;font-size:13px;line-height:1.45;color:#777}
.team-social{margin-top:12px;display:flex;gap:8px;justify-content:center}
.team-social span{width:26px;height:26px;border:1px solid #999;border-radius:50%}
.team-arrow{top:3250px}
/* contact */
.contact{left:0;top:3620px;width:1200px;height:520px;background:linear-gradient(180deg,#8fae2a,#6f8e18)}
.contact-title{left:0;top:3660px;width:1200px;text-align:center;font-size:40px;color:var(--white)}
.contact-title .divider{margin:12px auto 0}
.field{height:44px;border:1px solid rgba(255,255,255,.55);background:rgba(255,255,255,.12);color:var(--white);font-size:15px;padding:11px 14px}
.field-msg{height:130px}
.submit{left:526px;top:4048px;width:150px;height:48px;background:#26362e;color:var(--white);font-size:16px;text-transform:none}
/* footer */
.site-footer{left:0;top:4140px;width:1200px;height:344px;background:var(--footer)}
.footer-brand{left:0;top:4182px;width:1200px;text-align:center;font-weight:600;font-size:80px;letter-spacing:4px;color:var(--white);line-height:1}
.footer-nav{left:0;top:4340px;width:1200px;display:flex;justify-content:center;gap:26px;font-family:"Fira Sans Condensed",sans-serif;font-weight:500;font-size:15px;color:var(--white);text-transform:uppercase}
.footer-social{left:0;top:4376px;width:1200px;display:flex;justify-content:center;gap:12px}
.footer-social span{width:30px;height:30px;border:1.5px solid var(--white);border-radius:50%}
.copyright{left:0;top:4428px;width:1200px;text-align:center;font-size:14px;color:#d8ddd9}
</style>
</head>
<body>

<header class="site-header abs">
  <div class="brand abs">PAWLYTIX</div>
  <nav class="main-nav abs">
    <span class="active">Home</span><span>Mission</span><span>Capabilities</span><span>Pawlytix is a joint venture</span><span>The Team</span><span>Contact Us</span>
  </nav>
</header>

<div class="hero-photo abs" role="img" aria-label="Veterinarians examining a large dog on a clinic table"></div>
<h1 class="hero-title abs">PAWLYTIX</h1>
<p class="hero-sub abs">Sed ut perspiciatis unde omnis iste natus error sit voluptatem accusantium doloremque</p>
<span class="btn hero-btn abs">Get in touch</span>
<div class="hero-dots abs"><span class="on"></span><span></span></div>

<div class="mission-photo rounded-photo abs" role="img" aria-label="Vet holding a small spaniel puppy"></div>
<h2 class="section-title mission-title abs">Our Mission
  <svg class="divider" width="44" height="10" viewBox="0 0 44 10"><rect x="0" y="0" width="44" height="3" fill="#7c9a1c"/><rect x="0" y="7" width="44" height="3" fill="#7c9a1c"/></svg>
</h2>
<p class="mission-copy abs">Pawlytix is deploying a Software as a Service (SaaS) platform to facilitate the <span class="g">Efficient Collection</span>, <span class="b">Transmission</span>, <span class="n">Secure Storage</span> and anonymised analysis of data integral to animal diagnostics.</p>

<section class="capabilities abs"></section>
<h2 class="section-title cap-title abs">Capabilities
  <svg class="divider" width="44" height="10" viewBox="0 0 44 10"><rect x="0" y="0" width="44" height="3" fill="#7c9a1c"/><rect x="0" y="7" width="44" height="3" fill="#7c9a1c"/></svg>
</h2>
<div class="cap-body abs">
  <p>Originally developed for the human market, the core platform has been deployed in several regions and has been used to securely process nearly 3 million cases. The platform has been actively used by leading private labs and a large network of regional laboratories.</p>
  <p class="lead">Turnkey Initial Veterinary Deployment – Animal Health &amp; Welfare Pathway</p>
  <p>Pawlytix is finalising the design of a bespoke platform to facilitate the collection and processing of data and tests for the Animal Health and Welfare Pathway. Key elements include:</p>
  <ul class="cap-list">
    <li><svg width="14" height="12" viewBox="0 0 14 12"><path d="M1 6l4 4 8-9" fill="none" stroke="#7c9a1c" stroke-width="2.4"/></svg>Facilitated data collection at the farm by vets</li>
    <li><svg width="14" height="12" viewBox="0 0 14 12"><path d="M1 6l4 4 8-9" fill="none" stroke="#7c9a1c" stroke-width="2.4"/></svg>Secure and efficient processing of test samples by labs</li>
    <li><svg width="14" height="12" viewBox="0 0 14 12"><path d="M1 6l4 4 8-9" fill="none" stroke="#7c9a1c" stroke-width="2.4"/></svg>Digital results reporting</li>
    <li><svg width="14" height="12" viewBox="0 0 14 12"><path d="M1 6l4 4 8-9" fill="none" stroke="#7c9a1c" stroke-width="2.4"/></svg>Invoice support</li>
    <li><svg width="14" height="12" viewBox="0 0 14 12"><path d="M1 6l4 4 8-9" fill="none" stroke="#7c9a1c" stroke-width="2.4"/></svg>Data analysis reporting</li>
  </ul>
  <p style="margin-bottom:2px">Interested parties seeking further information should contact us at</p>
  <span class="cap-mail">info@pawlytix.com</span>
</div>
<div class="cap-photo rounded-photo abs" role="img" aria-label="Vet in green scrubs working with dairy cows in a barn"></div>

<section class="jv abs"></section>
<div class="jv-photo abs" role="img" aria-label="Vet examining a dog, tinted blue"></div>
<h2 class="section-title jv-title abs">Pawlytix is a joint venture
  <svg class="divider" width="44" height="10" viewBox="0 0 44 10"><rect x="0" y="0" width="44" height="3" fill="#7c9a1c"/><rect x="0" y="7" width="44" height="3" fill="#7c9a1c"/></svg>
</h2>
<div class="jv-copy abs">
  <p>Northfield Solutions Limited (NSL), an innovative veterinary led, close to market and scalable food research organisation. NSL brings together a team of highly experienced vets representing key opinion leaders within the livestock industry and additional technical support staff through its shareholder practices across the region, each a long established mixed veterinary group with an independent network of practices across the country.</p>
  <p>Clearpath Diagnostics Limited (CDL) is a rapidly growing Software as a Service platform provider in the digital health market. CDL adopts an agile and collaborative software development process working in partnership with its clients, using partners to build the best solutions as effectively and efficiently as possible.</p>
</div>

<h2 class="section-title team-title abs">The Team
  <svg class="divider" width="44" height="10" viewBox="0 0 44 10"><rect x="0" y="0" width="44" height="3" fill="#7c9a1c"/><rect x="0" y="7" width="44" height="3" fill="#7c9a1c"/></svg>
</h2>
<svg class="team-arrow abs" style="left:48px" width="20" height="60" viewBox="0 0 20 60"><path d="M18 2L3 30l15 28" fill="none" stroke="#bbb" stroke-width="2"/></svg>
<svg class="team-arrow abs" style="left:1132px" width="20" height="60" viewBox="0 0 20 60"><path d="M2 2l15 28L2 58" fill="none" stroke="#bbb" stroke-width="2"/></svg>

<article class="team-card abs" style="left:108px">
  <div class="team-photo" role="img" aria-label="Portrait of a smiling team member"></div>
  <h3 class="team-name">ALEX MORGAN</h3>
  <p class="team-bio">Sed ut perspiciatis unde om niste natus error sit</p>
  <div class="team-social"><span></span><span></span></div>
</article>
<article class="team-card abs" style="left:360px">
  <div class="team-photo" role="img" aria-label="Portrait of a smiling team member"></div>
  <h3 class="team-name">ALEX MORGAN</h3>
  <p class="team-bio">Sed ut perspiciatis unde om niste natus error sit</p>
  <div class="team-social"><span></span><span></span></div>
</article>
<article class="team-card abs" style="left:612px">
  <div class="team-photo" role="img" aria-label="Portrait of a smiling team member"></div>
  <h3 class="team-name">ALEX MORGAN</h3>
  <p class="team-bio">Sed ut perspiciatis unde om niste natus error sit</p>
  <div class="team-social"><span></span><span></span></div>
</article>
<article class="team-card abs" style="left:864px">
  <div class="team-photo" role="img" aria-label="Portrait of a smiling team member"></div>
  <h3 class="team-name">ALEX MORGAN</h3>
  <p class="team-bio">Sed ut perspiciatis unde om niste natus error sit</p>
  <div class="team-social"><span></span><span></span></div>
</article>

<section class="contact abs" role="img" aria-label="Green tinted background of a vet with a dog"></section>
<h2 class="section-title contact-title abs">Contact Us
  <svg class="divider" width="44" height="10" viewBox="0 0 44 10"><rect x="0" y="0" width="44" height="3" fill="#ffffff"/><rect x="0" y="7" width="44" height="3" fill="#ffffff"/></svg>
</h2>
<div class="field abs" style="left:276px;top:3750px;width:300px">First Name :</div>
<div class="field abs" style="left:600px;top:3750px;width:320px">Last Name :</div>
<div class="field abs" style="left:276px;top:3816px;width:300px">Email :</div>
<div class="field abs" style="left:600px;top:3816px;width:320px">Phone :</div>
<div class="field field-msg abs" style="left:276px;top:3882px;width:644px">Message :</div>
<span class="btn submit abs">Submit</span>

<footer class="site-footer abs"></footer>
<div class="footer-brand abs">PAWLYTIX</div>
<nav class="footer-nav abs"><span>Home</span><span>Mission</span><span>Capabilities</span><span>Pawlytix is a joint venture</span><span>The Team</span><span>Contact Us</span></nav>
<div class="footer-social abs"><span></span><span></span><span></span><span></span><span></span></div>
<p class="copyright abs">© Copyright 2022 Pawlytix All Rights Reserved</p>

</body>
</html>
```